DMR Property - Business Cards

Looking for a business card & general letterhead, signage etc design for our new logo.

Colours:
000a20
0056a2
00b5ef
0088ce
68cef2

Fonts:
Poppins
Karla

Please keep look and feel of new brand - example in the zip package I sent.

```html
<!DOCTYPE html>
<html lang="en">
<head>
<meta charset="utf-8">
<title>DMR Property – Business Cards</title>
<link rel="stylesheet" href="https://fonts.googleapis.com/css2?family=Poppins:wght@300;400;600;700&family=Karla:wght@400;500&display=swap">
<style>
  :root {
    --navy: #000a20;
    --card-navy: #121629;
    --deep-blue: #0056a2;
    --sky: #00b5ef;
    --mid-blue: #0088ce;
    --light-blue: #68cef2;
    --paper: #ffffff;
    --ink: #4a4f5a;
    --stage: #e6e9ef;
  }
  * { box-sizing: border-box; margin: 0; padding: 0; }
  html, body {
    width: 1200px; height: 800px; overflow: hidden;
    background: var(--stage);
  }
  .canvas {
    width: 1200px; height: 800px;
    display: flex; align-items: center; justify-content: center; gap: 40px;
  }
  .card {
    position: relative;
    width: 520px; height: 300px;
    border-radius: 26px;
    overflow: hidden;
    box-shadow: 0 12px 30px rgba(0, 10, 32, 0.18);
  }
  /* back */
  .card-back {
    background: var(--card-navy);
    display: flex; align-items: center; justify-content: center;
  }
  .brand {
    display: flex; align-items: center; gap: 12px;
    font-family: "Poppins", sans-serif;
    font-weight: 700;
    letter-spacing: 0.02em;
    white-space: nowrap;
  }
  .brand-dot { border-radius: 50%; flex: none; }
  .card-back .brand { color: var(--mid-blue); font-size: 44px; }
  .card-back .brand-dot { width: 26px; height: 26px; background: var(--mid-blue); }
  /* front */
  .card-front { background: var(--paper); }
  .front-sweep { position: absolute; inset: 0; width: 100%; height: 100%; }
  .card-front .brand {
    position: absolute; left: 34px; top: 44px;
    color: var(--deep-blue); font-size: 26px; gap: 9px;
  }
  .card-front .brand-dot { width: 16px; height: 16px; background: var(--deep-blue); }
  .person {
    position: absolute; left: 250px; top: 104px;
    font-family: "Poppins", sans-serif;
  }
  .person-name {
    color: var(--deep-blue); font-weight: 700; font-size: 21px;
    letter-spacing: 0.01em; text-transform: uppercase;
  }
  .person-title {
    color: var(--light-blue); font-weight: 400; font-size: 15px; margin-top: 2px;
  }
  .contact {
    position: absolute; left: 34px; bottom: 30px;
    font-family: "Karla", sans-serif; font-size: 14px; line-height: 1.45;
    color: var(--ink); list-style: none;
  }
  .contact li { display: flex; align-items: center; gap: 8px; }
  .contact .address { padding-left: 22px; margin-bottom: 2px; }
  .contact-icon { width: 14px; height: 14px; flex: none; }
</style>
</head>
<body>
<main class="canvas">
  <section class="card card-back" aria-label="Business card back">
    <div class="brand"><span class="brand-dot"></span>DMR PROPERTY</div>
  </section>

  <section class="card card-front" aria-label="Business card front">
    <svg class="front-sweep" viewBox="0 0 520 300" preserveAspectRatio="none" aria-hidden="true">
      <path d="M290 0 H520 V300 H478 C472 150 420 40 290 0 Z" fill="#1f9ae0"/>
      <path d="M318 10 C430 40 488 150 492 300 H476 C470 170 428 62 318 10 Z" fill="var(--light-blue)"/>
      <path d="M318 10 C428 62 470 170 476 300 H468 C462 175 420 70 318 10 Z" fill="#fff"/>
    </svg>

    <div class="brand"><span class="brand-dot"></span>DMR PROPERTY</div>

    <div class="person">
      <p class="person-name">Aldren Veskor</p>
      <p class="person-title">Managing Director</p>
    </div>

    <ul class="contact">
      <li class="address">218 W Harlow St Oakridge,<br>CA 90210</li>
      <li>
        <svg class="contact-icon" viewBox="0 0 16 16" aria-hidden="true"><circle cx="8" cy="8" r="8" fill="var(--deep-blue)"/><path d="M5 4.5c.6-.4 1.1-.2 1.4.4l.5 1c.2.4 0 .8-.3 1l-.4.3c.4.9 1 1.5 1.9 1.9l.3-.4c.3-.3.7-.4 1-.2l1 .5c.6.3.7.9.3 1.4-.6.8-1.6 1-2.5.5C6.4 10.3 5.4 9.3 4.8 7.5c-.3-1 0-2.3.2-3z" fill="#fff"/></svg>
        (555) 014-2290
      </li>
      <li>
        <svg class="contact-icon" viewBox="0 0 16 16" aria-hidden="true"><circle cx="8" cy="8" r="8" fill="var(--deep-blue)"/><rect x="4" y="5" width="8" height="6" rx="1" fill="#fff"/><path d="M4.3 5.4 8 8.3l3.7-2.9" stroke="var(--deep-blue)" stroke-width="1" fill="none"/></svg>
        info@dmrproperty.com
      </li>
      <li>
        <svg class="contact-icon" viewBox="0 0 16 16" aria-hidden="true"><circle cx="8" cy="8" r="8" fill="var(--deep-blue)"/><circle cx="8" cy="8" r="4.2" stroke="#fff" stroke-width="1" fill="none"/><path d="M3.8 8h8.4M8 3.8c-1.6 2.4-1.6 6 0 8.4M8 3.8c1.6 2.4 1.6 6 0 8.4" stroke="#fff" stroke-width=".9" fill="none"/></svg>
        www.dmrproperty.com
      </li>
    </ul>
  </section>
</main>
</body>
</html>
```